Business Card for Willowcrest Terrain Advisors

We need a business card for Willowcrest Terrain Advisors. The company website address is provided below. The company logo is attached. We provide specialized permafrost services to the mining, transportation, and oil & gas industries. The card should be prepared for:
Dominic Halloway, PhD.
Willowcrest Terrain Advisors
PO Box 418529
Birch Hollow, Alaska 99612
Direct: +1-907-555-2964
Email: dhalloway@terrainadvisors-example.com
Website: www.willowcrestterrainadvisors-example.com

```html
<!DOCTYPE html>
<html lang="en">
<head>
<meta charset="utf-8">
<title>Willowcrest Terrain Advisors – Business Card</title>
<link rel="stylesheet" href="https://fonts.googleapis.com/css2?family=Montserrat:wght@400;600;700&display=swap">
<style>
  :root {
    --page-bg: #e4e5e8;
    --card-white: #ffffff;
    --card-navy: #141e2a;
    --ink: #1a2431;
    --ink-soft: #3a434f;
    --rule: #9aa0a8;
    --silver: #d6d9dd;
  }
  * { box-sizing: border-box; margin: 0; padding: 0; }
  html, body {
    width: 1200px; height: 1200px; overflow: hidden;
    background: var(--page-bg);
    font-family: "Montserrat", Arial, sans-serif;
  }
  .sheet {
    width: 1200px; height: 1200px;
    display: flex; flex-direction: column; align-items: center; justify-content: center;
    gap: 52px;
  }
  .card {
    position: relative;
    width: 900px; height: 514px;
    border-radius: 40px;
    box-shadow: 0 10px 28px rgba(0,0,0,0.18);
    overflow: hidden;
  }
  .card--front { background: var(--card-white); color: var(--ink); }
  .card--back {
    background: radial-gradient(ellipse at 50% 40%, #1d2a3a 0%, var(--card-navy) 70%);
    display: flex; align-items: center; justify-content: center;
  }
  .brand-name {
    font-weight: 700;
    text-transform: uppercase;
    letter-spacing: 0.06em;
    text-align: center;
    line-height: 1.1;
  }
  .card--front .brand-name {
    position: absolute; left: 120px; top: 96px; width: 660px;
    font-size: 44px; color: var(--ink);
  }
  .card--back .brand-name {
    font-size: 50px; color: var(--silver); width: 700px;
  }
  .divider {
    position: absolute; left: 452px; top: 270px;
    width: 1px; height: 170px; background: var(--rule);
  }
  .holder {
    position: absolute; left: 60px; top: 372px; width: 370px;
    text-align: right;
  }
  .holder__name {
    font-size: 22px; font-weight: 700; text-transform: uppercase; color: var(--ink-soft);
  }
  .holder__company {
    font-size: 14px; font-weight: 600; text-transform: uppercase; color: var(--ink-soft);
    margin-top: 2px;
  }
  .contact-list {
    position: absolute; left: 480px; top: 272px;
    list-style: none;
    font-size: 15.5px; color: var(--ink-soft);
  }
  .contact-list li {
    display: flex; align-items: flex-start; gap: 10px;
    line-height: 1.25; margin-bottom: 8px;
  }
  .contact-list svg { flex: none; width: 18px; height: 18px; margin-top: 1px; fill: var(--ink); }
</style>
</head>
<body>
<main class="sheet">
  <section class="card card--front">
    <div class="brand-name">Willowcrest Terrain Advisors</div>
    <div class="divider"></div>
    <div class="holder">
      <p class="holder__name">Dominic Halloway, PhD</p>
      <p class="holder__company">Willowcrest Terrain Advisors</p>
    </div>
    <ul class="contact-list">
      <li>
        <svg viewBox="0 0 24 24"><path d="M6.6 10.8a15.1 15.1 0 0 0 6.6 6.6l2.2-2.2a1 1 0 0 1 1-.25 11.4 11.4 0 0 0 3.6.57 1 1 0 0 1 1 1V20a1 1 0 0 1-1 1A17 17 0 0 1 3 4a1 1 0 0 1 1-1h3.5a1 1 0 0 1 1 1c0 1.25.2 2.45.57 3.57a1 1 0 0 1-.25 1z"/></svg>
        <span>+1-907-555-2964</span>
      </li>
      <li>
        <svg viewBox="0 0 24 24"><path d="M12 2a7 7 0 0 0-7 7c0 5.2 7 13 7 13s7-7.8 7-13a7 7 0 0 0-7-7zm0 9.5A2.5 2.5 0 1 1 12 6.5a2.5 2.5 0 0 1 0 5z"/></svg>
        <span>PO Box 418529<br>Birch Hollow, Alaska 99612</span>
      </li>
      <li>
        <svg viewBox="0 0 24 24"><path d="M12 2a10 10 0 1 0 0 20 10 10 0 0 0 0-20zm6.9 6h-2.9a15.6 15.6 0 0 0-1.4-3.6A8 8 0 0 1 18.9 8zM12 4c.8 1.2 1.5 2.5 1.9 4h-3.8c.4-1.5 1.1-2.8 1.9-4zM4.3 14a8 8 0 0 1 0-4h3.4a16 16 0 0 0 0 4zm.8 2h2.9c.3 1.3.8 2.5 1.4 3.6A8 8 0 0 1 5.1 16zM8 8H5.1a8 8 0 0 1 4.3-3.6C8.8 5.5 8.3 6.7 8 8zm4 12c-.8-1.2-1.5-2.5-1.9-4h3.8c-.4 1.5-1.1 2.8-1.9 4zm2.3-6H9.7a14.7 14.7 0 0 1 0-4h4.6a14.7 14.7 0 0 1 0 4zm.3 5.6c.6-1.1 1.1-2.3 1.4-3.6h2.9a8 8 0 0 1-4.3 3.6zm1.7-5.6a16 16 0 0 0 0-4h3.4a8 8 0 0 1 0 4z"/></svg>
        <span>www.willowcrestterrainadvisors-example.com</span>
      </li>
      <li>
        <svg viewBox="0 0 24 24"><path d="M3 5h18a1 1 0 0 1 1 1v12a1 1 0 0 1-1 1H3a1 1 0 0 1-1-1V6a1 1 0 0 1 1-1zm1 2.4V17h16V7.4l-8 5.2z"/></svg>
        <span>dhalloway@terrainadvisors-example.com</span>
      </li>
    </ul>
  </section>

  <section class="card card--back">
    <div class="brand-name">Willowcrest Terrain Advisors</div>
  </section>
</main>
</body>
</html>
```